Graphic Design 4x 960x360 REVOULTION SLIDERS for Design Project for Lumora Nutrition

Hi,

I want to update my website sliders to make it look more sports nutrition related and more fitting for my business. You can view my website at www.lumoranutrition-example.com and I would like 4 sliders for the site. Read my blogs too to learn more about what I do.

I would like to highlight my logo and my tag line within my logo of happy, healthy, and oxygenated. Pictures of me intertwined in sliders ok as well.

Revolution Slides size: 960x360 PLEASE REVIEW THIS SAMPLE VERSION of the slides I like and similar. PLEASE REVIEW FILE #2 THANK You. :)

Additionally, some words I like are TideTurner on a slide.
Recovery and Rebound, and the theme and main meaning of Lumora (Happiness, Healthy, and Oxygen) all realated to fitness, health, medical nutritional therapy.

Thank you so much and looking forward!

Hi everyone, 

Hope your all doing great. I updated a File #2 slide for you to review on an example of the slides and style I like. Thank you for all your hard work! 

Hi all,

Hope all is well. I wanted to guide you more on a 2 slides. I am interested in a slide that has a beach theme and happy, healthy, and fitness people working out in the background playing volleyball, surfing, and running. Also eating some fruit would be nice. Then another slide with Lumora Nutrition on  a billboard and the billboard looking with healthy and happy. Maybe symbol on there and more dynamic feelings around that. Thanks again and I extended the date. Hope this update helps. 

Reason: I am still looking for the perfect design. The newest ones are on the right track. I appreciate everyone so much. Lots of health, happiness, and oxygen.

Hello Everyone,

I hope all is well. I am going to extend the project because I am going on a business trip. PLease review some of the updates I did to the main aspect and some attachments I did add as well. 

Reason: Would love to see you shine in your creativity within the business.

Reason: I would love to see other options and the big billboard Of lumora Nutrition. I have been out of town so I apologize for not making updates. please let me know if your interested and submit some designs. thank you your beautiful!

hello all,

I would love if you could make a slide that states to visit the Lumora Nutrition Online store. 

To schedule appointments and order the best quality supplements. 
QBV Approved for Athletics

Reason: I would love to extend this so we can move forward. Thank you.

Target Market(s)

Happy, Healthy, Sports, fitness, medical, and sports professionals

Industry/Entity Type

Nutrition

Requirements
Must have
• Theme and Logo of Lumora Nutrition.

```html
<!DOCTYPE html>
<html lang="en">
<head>
<meta charset="utf-8">
<title>Lumora Nutrition – Slider</title>
<link rel="stylesheet" href="https://fonts.googleapis.com/css2?family=Open+Sans:wght@600;700&display=swap">
<style>
  :root {
    --mat: #52565e;
    --white: #ffffff;
    --blue-deep: #0b2a8f;
    --blue-mid: #1440b8;
    --blue-light: #2a63dc;
    --brand-blue: #1d3f96;
    --brand-green: #5aa22c;
    --tagline-grey: #55585e;
    --photo-warm: #d9b7a0;
    --photo-sky: #cfe3f3;
  }
  * { margin: 0; padding: 0; box-sizing: border-box; }
  html, body {
    width: 1200px; height: 750px; overflow: hidden;
    background: var(--mat);
    font-family: "Open Sans", Arial, sans-serif;
  }
  .slider {
    position: absolute; left: 120px; top: 195px;
    width: 960px; height: 360px; overflow: hidden;
  }
  .slider-bg { position: absolute; inset: 0; }
  .brand {
    position: absolute; left: 30px; top: 112px;
    display: flex; align-items: center; gap: 16px;
  }
  .brand-dot {
    width: 44px; height: 44px; border-radius: 50%;
    background: var(--brand-green);
  }
  .brand-name {
    font-size: 60px; font-weight: 700; line-height: 1;
    color: var(--brand-blue); letter-spacing: -1px;
  }
  .tagline {
    position: absolute; left: 0; width: 346px; top: 263px;
    text-align: center; color: var(--tagline-grey);
    font-size: 17px; font-weight: 600; letter-spacing: 0.6px;
    line-height: 25px; text-transform: uppercase;
  }
  .pillar {
    position: absolute; top: 65px; width: 180px;
    display: flex; flex-direction: column; align-items: center;
  }
  .pillar-photo {
    width: 176px; height: 176px; border-radius: 50%;
    border: 4px solid var(--white);
    box-shadow: 0 2px 8px rgba(0,0,0,0.3);
  }
  .pillar-photo.warm { background: radial-gradient(circle at 50% 40%, #e8cbb5, var(--photo-warm) 55%, #b98c6f); }
  .pillar-photo.studio { background: radial-gradient(circle at 50% 45%, #e6d2c4, #c9a991 55%, #9d8a7d); }
  .pillar-photo.sky { background: radial-gradient(circle at 50% 45%, #f1e2d6, var(--photo-sky) 60%, #a9c9e6); }
  .pillar-label {
    margin-top: 20px; color: var(--white);
    font-size: 37px; font-weight: 700; line-height: 1;
    text-shadow: 0 2px 4px rgba(0,0,0,0.35);
  }
</style>
</head>
<body>
  <section class="slider">
    <svg class="slider-bg" width="960" height="360" viewBox="0 0 960 360" aria-hidden="true">
      <defs>
        <linearGradient id="blueField" x1="0" y1="0" x2="1" y2="0.4">
          <stop offset="0" stop-color="var(--blue-deep)"/>
          <stop offset="0.55" stop-color="var(--blue-mid)"/>
          <stop offset="1" stop-color="var(--blue-light)"/>
        </linearGradient>
        <linearGradient id="sheen" x1="0" y1="0" x2="1" y2="0">
          <stop offset="0" stop-color="#ffffff" stop-opacity="0"/>
          <stop offset="0.5" stop-color="#ffffff" stop-opacity="0.12"/>
          <stop offset="1" stop-color="#ffffff" stop-opacity="0"/>
        </linearGradient>
      </defs>
      <rect width="960" height="360" fill="url(#blueField)"/>
      <path d="M560 0 C620 120 600 240 640 360 L720 360 C690 240 700 120 640 0 Z" fill="url(#sheen)"/>
      <path d="M800 0 C850 120 840 250 880 360 L960 360 L960 120 C920 80 900 40 880 0 Z" fill="url(#sheen)"/>
      <path d="M0 0 L335 0 C378 110 378 250 322 360 L0 360 Z" fill="var(--white)"/>
    </svg>

    <div class="brand">
      <span class="brand-dot"></span>
      <span class="brand-name">Lumora</span>
    </div>
    <p class="tagline">Nutrition for<br>Sports, Fitness and Life</p>

    <div class="pillar" style="left:390px">
      <div class="pillar-photo warm" role="img" aria-label="Smiling woman raising her arms in celebration"></div>
      <span class="pillar-label">happy</span>
    </div>
    <div class="pillar" style="left:582px">
      <div class="pillar-photo studio" role="img" aria-label="Smiling woman doing a fitness workout in a studio"></div>
      <span class="pillar-label">healthy</span>
    </div>
    <div class="pillar" style="left:772px">
      <div class="pillar-photo sky" role="img" aria-label="Woman with open arms breathing fresh air under a bright sky"></div>
      <span class="pillar-label">oxygen</span>
    </div>
  </section>
</body>
</html>
```